CD-/Plattencover für Musikalbum
Zielgruppe
Wir sind eine Tonträgerfirma und bewegen uns im Low-Budget-Segment.
Aufgabenstellung
Artwork-Design (Cover) für ein Musikalbum : „Tanzabendzauber”
Wir benötigen nicht das komplette Artwork, sondern ein Frontcover
(121 x 120 mm + 20 mm Beschnitt) wg. etwaiger Verschiebung der Positionierung.
Fertigstellung (Aufziehen des Inlays und Labels) erfolgt später bei uns im Hause.
Wir benötigen später eine offene psd-Datei mit allen Ebenen.
Wichtig: Schriften nicht gerastert ggfs. Schrift mitliefern.
Was wir uns vorstellen:
- Entsprechend der Musik Bild, Tracks Beispiele:
Bis zum letzten Wintertag
Ein Brief, der meine Sehnsucht kennt
Ganz leise Sommerzeit
Die Nacht wird hell
Karl, komm tanz mit mir heut
- Bildmaterial sollte bei pixelhafen, bildora oder q-motiv ausgesucht werden, das Bildmaterial wird dann später auch von uns dort eingekauft.
- keine Künstlerfotos.

```html
<!DOCTYPE html>
<html lang="de">
<head>
<meta charset="utf-8">
<title>Tanzabendzauber – Frontcover</title>
<link rel="stylesheet" href="https://fonts.googleapis.com/css2?family=Chewy&family=Open+Sans:wght@700&display=swap">
<style>
  :root {
    --night: #0d0c14;
    --mirror-dark: #2a2a36;
    --mirror-mid: #6c6f7e;
    --mirror-light: #c9ccd6;
    --violet-glow: #4a2f8a;
    --disc-white: rgba(255, 255, 255, 0.86);
    --ring-white: #ffffff;
    --ring-soft: rgba(210, 210, 220, 0.7);
    --title-pink: #d01455;
    --title-shadow: #2a1a1e;
    --track-ink: #141414;
  }
  html, body {
    margin: 0;
    padding: 0;
    overflow: hidden;
    background: var(--night);
  }
  .cover {
    position: relative;
    width: 1200px;
    height: 1190px;
    overflow: hidden;
  }
  .cover__photo {
    position: absolute;
    inset: 0;
    background:
      radial-gradient(circle at 20% 25%, var(--mirror-light) 0%, rgba(201,204,214,0) 28%),
      radial-gradient(circle at 85% 20%, var(--mirror-mid) 0%, rgba(108,111,126,0) 30%),
      radial-gradient(circle at 10% 85%, var(--violet-glow) 0%, rgba(74,47,138,0) 30%),
      radial-gradient(circle at 90% 80%, var(--mirror-mid) 0%, rgba(108,111,126,0) 32%),
      linear-gradient(135deg, var(--mirror-dark) 0%, var(--night) 55%, var(--mirror-dark) 100%);
  }
  .cover__rings {
    position: absolute;
    inset: 0;
  }
  .cover__title {
    position: absolute;
    left: 0;
    top: 330px;
    width: 1200px;
    text-align: center;
    font-family: "Chewy", "Comic Sans MS", cursive;
    color: var(--title-pink);
    font-size: 160px;
    line-height: 150px;
    margin: 0;
    font-weight: 400;
    transform: rotate(-5deg);
    text-shadow: 4px 4px 0 var(--title-shadow), 7px 7px 0 var(--title-shadow), 10px 10px 0 var(--title-shadow);
    letter-spacing: 2px;
  }
  .cover__title span { display: block; }
  .cover__tracks {
    position: absolute;
    left: 0;
    top: 728px;
    width: 1258px;
    margin: 0;
    padding: 0;
    list-style: none;
    text-align: center;
    font-family: "Open Sans", Arial, sans-serif;
    font-weight: 700;
    font-size: 25px;
    line-height: 37.5px;
    color: var(--track-ink);
  }
</style>
</head>
<body>
  <main class="cover">
    <div class="cover__photo" role="img" aria-label="Nahaufnahme glitzernder Discokugeln mit Spiegelfacetten und violettem Licht"></div>

    <svg class="cover__rings" width="1200" height="1190" viewBox="0 0 1200 1190" aria-hidden="true">
      <circle class="disc" cx="629" cy="612" r="403" fill="var(--disc-white)"/>
      <circle class="ring-soft" cx="612" cy="590" r="462" fill="none" stroke="var(--ring-soft)" stroke-width="6"/>
      <circle class="ring-outer" cx="624" cy="604" r="503" fill="none" stroke="var(--ring-white)" stroke-width="5"/>
    </svg>

    <h1 class="cover__title"><span>Tanzabend</span><span>zauber</span></h1>

    <ul class="cover__tracks">
      <li>u.a. Ein Brief, der meine Sehnsucht kennt</li>
      <li>Bis zum letzten Wintertag&nbsp;&nbsp;Die Nacht wird hell</li>
      <li>Karl, komm tanz mit mir heut</li>
      <li>Ganz leise Sommerzeit …</li>
    </ul>
  </main>
</body>
</html>
```